Herb Farm - Tea Label Design

We are a small herbalist company called 'Meadowlark Remedies' which requires a new label scheme.

Meadowlark Remedies specializes in organic wellness teas, handmade soaps, bath and beauty products. We also offer local beeswax, pollen and an herb CSA.

Our slogan is "Old Wisdom for Everyday Living" and we frequently market ourselves as an "Apothecary & Herb Farm".

The primary use of this label will be on tins and biodegradable food grade paper bags.

We are looking for:

1) An unique universal design for our products. Something that we can put on the tea tins/bags as well as boxes in the future. To keep costs down I would like something that can be used on a variety of products by simply having the colour changed or adding the title of the product in a certain area. We have four collections. Please see the attached style guide. I particularly like the Silverbrook Leaf Co. as each type of tea is reprinted by a design. Please see their website for further clarification. I also really like their styling.

2) Label required is 8.5" x 5.25" (w - h). Bear in mind we also have dark cobalt blue jars and Kraft biodegradable bags available that this label will fit on (5570-02 as pictured)

3) We would like to see a design that is colourful, and has elements of modern simplicity yet certainly has an old world apothecary charm.

4) Please refer to our current label for product information. Not everything has to be in the same place in the new design, however all the information is required.

We will require source files in .ai and .eps (layers retained, no outlines on text, list of fonts used).

Please visit: www.meadowlarkremedies.example

We included a few favourites and the styles we prefer, but please be creative!

The label chosen could be in for a lot more design work as we expand our company. Any other input regarding packaging would be helpful.
Updates

Hello Designers!

I have posted our current label for you to review - I like it, yet I don't. You can see the level of craftsman ship brings up to artisan, and mid-high range product. The only parts I really want to keep from this label is how the brewing instructions are set out.

In terms of design, I do not want to use a photograph on the label - it is there for inspiration!

Thanks,
Meadowlark Remedies 

Reason: I would like to see more designs, from a variety of designers for this label project.

Reason: Would like to see more designs.

Reason: In receiving designs I realized that the sizing is not ideal as it does not have ample space for the required information. I have updated the brief to reflect this and posted a working file that has the required elements. A lot of good designs, but I noticed the over use of filigree or Victorian ornamentation. I would like some ornamentation but simplicity is desired in the overall label. There was not enough designs submitted, nothing that truly wow-ed me. I hope to see more unique designs! Thanks.

Target Market(s)

30-something, retired, eco-conscious, women, mid-priced marketing, local Ontario Canada; some products will be sold at a local historical village

Industry/Entity Type

Biodegradable

Font styles to use
Decorative
Other font styles liked:
• DellaRobbia BT Bold; Foglihten No07

Requirements
Must have
• Fonts used: Dellarobbia BT Bold and Foglihten No07
Use fonts and logo design; you can use separate leaf components but fonts chosen for logo cannot change

Other fonts can be used but please use Foglihten No07 for "Meadowlark Remedies" and Dellarobbia BT Bold for "Apothecary & Herb Farm" and for "Old Wisdom for Everyday Living".
Nice to have
• "Apothecary & Herb Farm" or slogan
Should not have
• Comic sans
clipart
Filigree or line swooshes

```html
<!DOCTYPE html>
<html lang="en">
<head>
<meta charset="utf-8">
<title>Meadowlark Remedies – Highland Haze Tea Label</title>
<link href="https://fonts.googleapis.com/css2?family=Source+Sans+3:wght@400;600&family=Courier+Prime&display=swap" rel="stylesheet">
<style>
  :root {
    --page: #f4f2ee;
    --label: #f3e4dc;
    --olive: #6b6a34;
    --olive-dark: #55542a;
    --band: #d5e4b1;
    --band-line: #6f7d3a;
    --sprig-a: #c98aa6;
    --sprig-b: #8fae5a;
    --ink: #4c4a2a;
  }
  * { box-sizing: border-box; margin: 0; padding: 0; }
  html, body { width: 1200px; height: 900px; overflow: hidden; }
  body { background: var(--page); font-family: "Source Sans 3", sans-serif; color: var(--olive); }
  .canvas { position: relative; width: 1200px; height: 900px; }

  .label {
    position: absolute; top: 112px; width: 380px; height: 676px;
    background: var(--label); text-align: center;
  }
  .label--front { left: 190px; }
  .label--back { left: 630px; }

  .brand { position: absolute; top: 92px; left: 0; right: 0; }
  .brand__name {
    font-weight: 600; font-size: 40px; line-height: 1.05; color: var(--olive);
  }
  .brand__tag { margin-top: 10px; font-size: 11px; letter-spacing: 4px; color: var(--olive); }

  .product-title { position: absolute; top: 318px; left: 0; right: 0; color: var(--olive); font-weight: 600; }
  .product-title__line1 { display: block; font-size: 36px; line-height: 1.1; }
  .product-title__line2 { display: block; font-size: 50px; line-height: 1.1; }

  .band {
    position: absolute; top: 480px; left: 0; right: 0; height: 78px;
    background: var(--band);
    border-top: 2px solid var(--band-line); border-bottom: 2px solid var(--band-line);
    display: flex; flex-direction: column; justify-content: center; align-items: center;
  }
  .band::before {
    content: ""; position: absolute; top: 2px; bottom: 2px; left: 0; right: 0;
    border-top: 1px solid var(--band-line); border-bottom: 1px solid var(--band-line);
    pointer-events: none;
  }
  .sprig {
    position: absolute; top: 22px; width: 46px; height: 30px; border-radius: 50%;
    background: linear-gradient(135deg, var(--sprig-a), var(--sprig-b));
    opacity: .75;
  }
  .sprig--left { left: 16px; }
  .sprig--right { right: 16px; }
  .band__byline { font-size: 19px; line-height: 1.2; color: var(--olive-dark); }
  .band__slogan { font-size: 13px; letter-spacing: 1.5px; color: var(--olive-dark); }
  .band__web { margin-top: 12px; font-size: 10px; letter-spacing: 1.5px; font-weight: 600; color: var(--olive-dark); }

  .net-weight { position: absolute; top: 640px; left: 0; right: 0; font-size: 14px; color: var(--ink); }

  .ingredients-head { position: absolute; top: 292px; left: 0; right: 0; font-size: 20px; letter-spacing: 4px; font-weight: 600; line-height: 1.3; }
  .ingredients-text {
    position: absolute; top: 370px; left: 34px; right: 34px;
    font-family: "Courier Prime", monospace; font-size: 13px; line-height: 1.35; color: var(--ink);
  }

  .brew { position: absolute; top: 600px; left: 80px; right: 60px; display: grid; grid-template-columns: 1fr 1fr; row-gap: 12px; font-size: 12px; color: var(--ink); }
  .brew__item { display: flex; align-items: center; gap: 8px; }
  .brew__item svg { flex: none; }
  .brew__spacer { width: 20px; flex: none; }
  .brew__time { line-height: 1; text-align: center; }
</style>
</head>
<body>
<main class="canvas">

  <section class="label label--front" aria-label="Front label">
    <div class="brand">
      <div class="brand__name">Meadowlark<br>Remedies</div>
      <div class="brand__tag">HEDGEROW HERB GARDEN</div>
    </div>
    <h1 class="product-title">
      <span class="product-title__line1">Highland</span>
      <span class="product-title__line2">Haze</span>
    </h1>
    <div class="band">
      <span class="sprig sprig--left" role="img" aria-label="Small painted herb sprig"></span>
      <div class="band__byline">By<br>Meadowlark Remedies</div>
      <span class="sprig sprig--right" role="img" aria-label="Small painted herb sprig"></span>
    </div>
    <p class="net-weight">NET WT. 15 g / 0.5 oz</p>
  </section>

  <section class="label label--back" aria-label="Back label">
    <div class="brand">
      <div class="brand__name">Meadowlark<br>Remedies</div>
      <div class="brand__tag">HEDGEROW HERB GARDEN</div>
    </div>
    <h2 class="ingredients-head">ORGANIC<br>INGREDIENTS</h2>
    <p class="ingredients-text">A floral infusion of white tea (Camellia sinensis)*, blueberries* elderberries*, cornflowers* and scotch heather*.<br>*organic</p>
    <div class="band">
      <span class="sprig sprig--left" role="img" aria-label="Small painted herb sprig"></span>
      <div class="band__slogan">Old Wisdom for Everyday Living</div>
      <div class="band__web">www.meadowlarkremedies.example</div>
      <span class="sprig sprig--right" role="img" aria-label="Small painted herb sprig"></span>
    </div>
    <div class="brew">
      <div class="brew__item">
        <svg width="20" height="20" viewBox="0 0 20 20" aria-hidden="true"><circle cx="10" cy="10" r="9" fill="var(--olive)"/><text x="10" y="14" text-anchor="middle" font-size="11" font-weight="700" fill="var(--label)" font-family="Source Sans 3, sans-serif">G</text></svg>
        <span>2.5 g / 1 tsp</span>
      </div>
      <div class="brew__item">
        <svg width="20" height="20" viewBox="0 0 20 20" aria-hidden="true"><circle cx="10" cy="10" r="8.5" fill="none" stroke="var(--olive)" stroke-width="1.4"/><path d="M10 5v5l-3 2" fill="none" stroke="var(--olive)" stroke-width="1.4"/></svg>
        <span class="brew__time">2 - 3<br>minutes</span>
      </div>
      <div class="brew__item">
        <svg width="20" height="20" viewBox="0 0 20 20" aria-hidden="true"><path d="M10 2C7 7 5 10 5 13a5 5 0 0 0 10 0c0-3-2-6-5-11z" fill="var(--olive)"/></svg>
        <span>80C / 185F</span>
      </div>
      <div class="brew__item">
        <span class="brew__spacer"></span>
        <span>177 mL / 6 oz</span>
      </div>
    </div>
  </section>

</main>
</body>
</html>
```